Webdesign K&M Lockenwerk
Zielgruppe
K&M Scherenkunst & Co. KG GmbH & Co. KG ist eine Firma, die u.a. Seminare und Schulungen für das Friseur- und Kosmetikhandwerk anbietet.
Weiterhin sind sie auch der Partner, wenn es um individuelle Saloneinrichtungen (Ladendesign und Einrichtung) geht.
Zielgruppen sind Friseurläden und Kosmetikstudios.
Aufgabenstellung
Das Layout bitte in Photoshop anlegen , es soll mit Wordpress umgesetzt werden.
Es soll keine Kopie der bestehenden Seite werden. Halten Sie sich strickt an die Vorgaben aus 'Welche Seiten sollen angezeigt werden'! Es geht in der neuen Seite ausschließlich um Schulungen & Seminare sowie Ladendesign & Einrichtungen.
Im header einen Slider andeuten.
Bei den Farben lassen wir Ihnen freien Lauf, allerdings soll es nich zu bunt werden.

```html
<!DOCTYPE html>
<html lang="de">
<head>
<meta charset="utf-8">
<title>K&amp;M Lockenwerk – Schulungen &amp; Ladendesign</title>
<link href="https://fonts.googleapis.com/css2?family=Merriweather:wght@300;400;700&display=swap" rel="stylesheet">
<style>
:root{
  --red:#c4262e;
  --red-dark:#a81d24;
  --ink:#3a3a3a;
  --text:#555;
  --light:#eeeeee;
  --nav:#f2f2f2;
  --topbar:#cfcfcf;
  --dark:#333333;
  --white:#fff;
}
*{box-sizing:border-box;margin:0;padding:0}
html,body{width:1200px;height:3798px;overflow:hidden}
body{font-family:"Merriweather",Georgia,serif;color:var(--ink);background:var(--light);position:relative}
.abs{position:absolute}
.btn{position:absolute;display:flex;align-items:center;justify-content:center;background:var(--red);color:var(--white);font-size:14px;border-radius:3px;box-shadow:0 2px 4px rgba(0,0,0,.2)}
.section-title{position:absolute;left:0;width:100%;text-align:center;color:var(--red);font-size:25px;font-weight:400;letter-spacing:.5px}

/* top bar + nav */
.topbar{position:absolute;left:0;top:0;width:1200px;height:24px;background:var(--topbar);font-size:10px;color:#555;letter-spacing:.5px}
.topbar .shop{position:absolute;left:228px;top:6px;display:flex;gap:8px;align-items:center}
.topbar .legal{position:absolute;right:175px;top:6px;display:flex;gap:8px;align-items:center}
.dot{width:9px;height:9px;border-radius:50%;background:#555;display:inline-block}
.nav{position:absolute;top:24px;left:0;width:1200px;height:75px;background:var(--nav);font-size:13px;letter-spacing:1px;color:#444}
.nav a{position:absolute;top:31px;text-decoration:none;color:inherit}
.brand-name{position:absolute;left:503px;top:25px;width:194px;text-align:center;font-size:18px;font-weight:400;letter-spacing:.5px;color:var(--ink)}

/* hero */
.hero{position:absolute;top:99px;left:0;width:1200px;height:451px;background:linear-gradient(90deg,#8a7a62 0%,#c9b58f 35%,#b8a58c 60%,#d9c6a6 100%)}
.hero .ribbon{position:absolute;left:128px;background:rgba(60,60,55,.85);color:var(--white);font-size:25px;padding:4px 15px;letter-spacing:.5px}
.hero p{position:absolute;left:142px;top:196px;width:290px;font-size:16px;line-height:22px;color:#222}
.dots{position:absolute;left:50%;bottom:14px;transform:translateX(-50%);display:flex;gap:8px}
.dots i{width:9px;height:9px;border-radius:50%;background:rgba(255,255,255,.6)}
.dots i:first-child{background:var(--white)}

/* seminars */
.intro{position:absolute;left:178px;top:631px;width:844px;text-align:center;font-size:12.5px;line-height:23px;color:var(--text)}
.card{position:absolute;top:761px;height:434px;background:#f4f4f4;box-shadow:0 3px 8px rgba(0,0,0,.2)}
.card .photo{height:203px}
.card h3{position:absolute;left:19px;top:218px;font-size:14.5px;font-weight:400;letter-spacing:.5px;line-height:23px;color:#333}
.card .trainer{position:absolute;left:19px;font-size:10px;color:var(--red)}
.card .desc{position:absolute;left:19px;right:19px;font-size:10.5px;line-height:16.5px;color:#666}
.card .signup{position:absolute;border-top:1px solid #555;border-bottom:1px solid #555;padding:7px 12px;font-size:13px;font-weight:700;letter-spacing:.5px;color:#333}
.card .signup small{color:var(--red);font-size:9px;font-weight:400}

/* design */
.design{position:absolute;top:1349px;left:0;width:1200px;height:656px;background:linear-gradient(180deg,#dcdcdc,#e6e6e6 50%,#d8d8d8)}
.design .copy{position:absolute;left:634px;width:405px;font-size:12.5px;line-height:23.5px;color:#555}

/* company */
.company .copy{position:absolute;left:167px;top:2133px;width:415px;font-size:12.5px;line-height:23.5px;color:#555}
.member{position:absolute;top:2108px;width:203px;height:264px;background:#f5f5f5;box-shadow:0 2px 6px rgba(0,0,0,.2);text-align:center}
.member .portrait{width:190px;height:190px;border-radius:50%;margin:3px auto 0}
.member .nm{margin-top:12px;font-size:17px;color:#333}
.member .role{font-size:12px;color:var(--red);margin-top:3px}

/* band */
.band{position:absolute;top:2506px;left:0;width:1200px;height:305px;background:radial-gradient(ellipse at 50% 20%,#d9363c,#b81f27 70%)}
.band .band-name{position:absolute;left:0;top:46px;width:100%;text-align:center;color:var(--white);font-size:26px;font-weight:400;letter-spacing:.5px}
.band p{position:absolute;left:0;top:117px;width:100%;text-align:center;color:var(--white);font-size:18.5px;line-height:33px}

/* newsletter */
.newsletter{position:absolute;top:2811px;left:0;width:1200px;height:476px;background:linear-gradient(90deg,#d4d4d4,#e4e4e4 50%,#cfcfcf)}
.field{position:absolute;left:220px;width:336px;height:45px;background:var(--white);border:1px solid #bbb;border-radius:3px;font-size:11px;color:#999;padding:15px 18px}

/* brands */
.brand{position:absolute;top:3408px;width:152px;height:125px;background:var(--white);display:flex;align-items:center;justify-content:center;font-size:19px;color:#777}
.cat{width:23px;height:23px;border-radius:50%;background:#555;border:2px solid #ccc}

/* footer */
.footer{position:absolute;top:3641px;left:0;width:1200px;height:157px;background:var(--dark);color:#ddd}
.footer nav{position:absolute;top:44px;left:0;width:100%;display:flex;justify-content:center;gap:26px;font-size:13px;letter-spacing:1px}
.footer .copy{position:absolute;left:178px;top:92px;font-size:9px}
.footer .legal{position:absolute;right:178px;top:92px;font-size:9px;display:flex;gap:12px}
.footer .social{position:absolute;left:583px;top:91px;display:flex;gap:8px}
.footer .social .dot{background:#ddd}
</style>
</head>
<body>

<header>
  <div class="topbar">
    <div class="shop">
      <svg width="14" height="12" viewBox="0 0 14 12"><path d="M0 1h3l2 7h7l1.5-5H4" fill="none" stroke="#555" stroke-width="1.3"/><circle cx="6" cy="10.5" r="1.2" fill="#555"/><circle cx="11" cy="10.5" r="1.2" fill="#555"/></svg>
      <span>ZUM SHOP</span>
    </div>
    <div class="legal"><span>IMPRESSUM</span>|<span>KONTAKT</span>|<span>DATENSCHUTZ</span>|<span class="dot"></span><span class="dot"></span></div>
  </div>
  <nav class="nav">
    <a style="left:225px">HOME</a>
    <a style="left:294px">SCHULUNGEN &amp; SEMINARE</a>
    <div class="brand-name">K&amp;M Lockenwerk</div>
    <a style="left:718px">LADENDESIGN &amp; EINRICHTUNGEN</a>
    <a style="left:986px">TEAM</a>
  </nav>
</header>

<section class="hero" role="img" aria-label="Friseurmeisterin frisiert eine junge Frau mit blonden Locken im Salon">
  <div class="ribbon" style="top:97px">MEISTERE DIE KUNST</div>
  <div class="ribbon" style="top:138px">DES FRISEURHANDWERKS</div>
  <p>Melden Sie sich für Schulungen und Seminare an, um die Feinheiten zu erfahren.</p>
  <div class="btn" style="left:139px;top:278px;width:162px;height:46px">Jetzt Anmelden</div>
  <div class="dots"><i></i><i></i><i></i></div>
</section>

<section class="seminars">
  <h2 class="section-title" style="top:586px">SCHULUNGEN &amp; SEMINARE</h2>
  <p class="intro">Weiterbildung ist ein fester Bestandteil für Qualität, Zuverlässigkeit und Kundenzufriedenheit und wir lernen ein Leben lang stets dazu. In der Region sind wir geschätzte Initiatoren von professionellen Seminaren für alle Angestellten oder Geschäftstreibenden im Friseur- und Kosmetikhandwerk sowie für Lehrlinge und Meisterschülerinnen und Meisterschüler. Wir begleiten und unterstützen Unterneh­mensgründer und Berufsanfänger ebenfalls.</p>

  <article class="card" style="left:147px;width:438px">
    <div class="photo" role="img" aria-label="Fachtrainerin zeigt einem Kunden ein Pflegeprodukt" style="background:linear-gradient(90deg,#6b5a4e,#c8b8a4 50%,#8f8a70)"></div>
    <h3>SALONSCHULUNG</h3>
    <div class="trainer" style="top:244px">Trainer: K&amp;M Trainerteam</div>
    <p class="desc" style="top:266px">Unsere Fachtrainer schulen Sie und Ihr Team. Ideal bei Wechsel des Herstellers/Produktes oder als Auffrischungskurs. Auf Wunsch in unseren Seminarräumen oder in Ihrem Salon. Wir sind spezialisiert auf Brillane, Velora, Artemis und Solvia. Ihr Außendienstmitarbeiter berät Sie gern.</p>
    <div class="signup" style="left:125px;top:380px">ANMELDUNG <small>(Auf Anfrage)</small></div>
  </article>

  <article class="card" style="left:619px;width:439px">
    <div class="photo" role="img" aria-label="Friseurin stylt lange gewellte Haare einer lächelnden Kundin" style="background:linear-gradient(90deg,#3e3438,#a9846a 50%,#4a4246)"></div>
    <h3>EINZELSCHULUNG EXTENTIONS-<br>HAARVERLÄNGERUNG / VERDICHTUNG</h3>
    <div class="trainer" style="top:268px">Trainer: K&amp;M Trainerteam</div>
    <p class="desc" style="top:290px">Einzelseminar für Einsteiger. Erlernen Sie die 3 Systeme, Bonding, Tape und Ringtechnik. Für jeden Einsatzzweck die richtige Technik. Ob nur für einen Abend oder als dauerhafte Haarverlängerung. Theorie und Praxisschulung am Übungskopf.</p>
    <div class="signup" style="left:132px;top:380px">ANMELDUNG <small>(€ 179 + 19% VAT)</small></div>
  </article>

  <div class="btn" style="left:516px;top:1250px;width:161px;height:44px">Mehr Lesen</div>
</section>

<section class="design" role="img" aria-label="Unscharfer Hintergrund eines hellen Salons">
  <div class="abs" role="img" aria-label="Friseurplatz mit Holzregal und Barbierstuhl" style="left:0;top:98px;width:271px;height:369px;background:linear-gradient(135deg,#c8c4bc,#7a6a5a 60%,#4a4038)"></div>
  <div class="abs" style="left:326px;top:125px;width:270px;height:411px;background:linear-gradient(180deg,#e43a40,#b81f27)"></div>
  <div class="abs" role="img" aria-label="Beleuchtete Frisierinsel mit schwarzen Salonstühlen" style="left:258px;top:156px;width:305px;height:407px;background:linear-gradient(180deg,#b9b9b4,#6f7a6a 45%,#2a2a2a)"></div>
  <h2 class="abs" style="left:634px;top:100px;color:var(--red);font-size:25px;font-weight:400">LADENDESIGN &amp; EINRICHTUNG</h2>
  <p class="copy" style="top:161px">Friseur-und Kosmetiksalons erheben den Anspruch, die Professionalität des Handwerks auf harmonische Art und Weise in Design und Inneneinrichtung widerzuspiegeln. K&amp;M löst Ihre Fragen vertrauensvoll und stilsicher – geben Sie Ihre Idee in professionelle Hände!</p>
  <p class="copy" style="top:300px">Wir entwerfen technische Zeichnungen, entwickeln effektive und stimmige Einrichtungskonzepte und veranlassen die entsprechende technische Aufbereitung und Umsetzung. Wir erledigen das gewünschte Bauvorhaben und die Bauleistungen oder die Sanierung von Gewerbeflächen entsprechend Ihrer Bedürfnisse und Visionen und erarbeiten mit Ihnen zusammen tragende Finanzierungskonzepte.</p>
  <div class="btn" style="left:631px;top:501px;width:227px;height:44px;font-size:13px">KONTAKT AUFNEHMEN</div>
</section>

<section class="company">
  <h2 class="abs" style="left:167px;top:2088px;color:var(--red);font-size:25px;font-weight:400">DAS UNTERNEHMEN K&amp;M</h2>
  <p class="copy">Kommen Sie vorbei und entdecken Sie die pflegenden und veredel­nden Möglichkeiten für Haar, Gesicht und Körper – für ein zufrie­denes Ich, einen glücklichen Kunden oder einfach für das private Wohlempfinden. Bei uns findet jede Art der Schönheit Beachtung! K&amp;M – das sind Menschen wie Sie und ich, die sich wohlfühlen, wenn Anmut, Style und Trends im neuen Glanze der Natürlichkeit erstrahlen.</p>
  <div class="btn" style="left:168px;top:2330px;width:152px;height:46px">Mehr Über K&amp;M</div>

  <div class="abs" style="left:588px;top:2083px;width:211px;height:217px;background:linear-gradient(180deg,#e43a40,#b81f27)"></div>
  <div class="member" style="left:612px">
    <div class="portrait" role="img" aria-label="Porträtfoto eines Vertriebsmitarbeiters" style="background:radial-gradient(circle,#c9a46e,#a98450)"></div>
    <div class="nm">Jonas Reitmeier</div><div class="role">Vertriebsrepräsentant</div>
  </div>
  <div class="abs" style="left:864px;top:2083px;width:211px;height:217px;background:linear-gradient(180deg,#e43a40,#b81f27)"></div>
  <div class="member" style="left:849px">
    <div class="portrait" role="img" aria-label="Porträtfoto einer Vertriebsmitarbeiterin" style="background:radial-gradient(circle,#eeeeee,#d6d6d6)"></div>
    <div class="nm">Sabine Kolb</div><div class="role">Vertriebsrepräsentantin</div>
  </div>
</section>

<section class="band" role="img" aria-label="Rote Fläche mit Friseurwerkzeugen wie Rundbürste, Schere und Lockenstab">
  <div class="band-name">K&amp;M Lockenwerk</div>
  <p>Besuchen Sie unseren Shop, um exklusive Marken in den Bereichen Kosmetik,<br>Einrichtung, Haarverlängerung und vieles mehr zu kaufen.</p>
  <div class="btn" style="left:525px;top:222px;width:152px;height:46px;background:#3a3a3a">Shop Besuchen</div>
</section>

<section class="newsletter" role="img" aria-label="Unscharfer Hintergrund eines Salons">
  <h2 class="abs" style="left:0;width:802px;top:85px;text-align:center;color:var(--red);font-size:24px;font-weight:400">JETZT BEITRETEN</h2>
  <p class="abs" style="left:0;width:802px;top:127px;text-align:center;font-size:17px;line-height:33px;color:#555">Abonnieren Sie unseren Newsletter, um die neuesten<br>Nachrichten und exklusiven Angebote zu erhalten.</p>
  <div class="field" style="top:220px">Name</div>
  <div class="field" style="top:284px">Email</div>
  <div class="btn" style="left:220px;top:348px;width:336px;height:44px;font-size:19px">Einreichen</div>
  <div class="abs" role="img" aria-label="Salonspiegel mit Trockenhaube und Blumendekoration" style="left:743px;top:71px;width:274px;height:353px;background:linear-gradient(160deg,#6a6a6c,#2c2c2e 55%,#8a5a7a)"></div>
  <div class="abs" style="left:716px;top:118px;width:89px;height:88px;background:rgba(196,38,46,.85)"></div>
  <div class="abs" style="left:790px;top:189px;width:38px;height:36px;background:rgba(196,38,46,.9)"></div>
</section>

<section class="brands">
  <h2 class="section-title" style="top:3333px">EXKLUSIVMARKEN</h2>
  <svg class="abs" style="left:105px;top:3458px" width="16" height="26" viewBox="0 0 16 26"><path d="M13 2 3 13l10 11" fill="none" stroke="#999" stroke-width="3"/></svg>
  <div class="brand" style="left:159px">Artemis</div>
  <div class="brand" style="left:342px">Velora</div>
  <div class="brand" style="left:524px">Lina Rosé</div>
  <div class="brand" style="left:707px">Coiffix</div>
  <div class="brand" style="left:889px">Brillane</div>
  <svg class="abs" style="left:1077px;top:3458px" width="16" height="26" viewBox="0 0 16 26"><path d="M3 2l10 11L3 24" fill="none" stroke="#999" stroke-width="3"/></svg>
  <div class="abs" style="left:516px;top:3577px;display:flex;gap:14px"><span class="cat"></span><span class="cat"></span><span class="cat"></span><span class="cat"></span><span class="cat"></span></div>
</section>

<footer class="footer">
  <nav><span>HOME</span><span>SCHULUNGEN &amp; SEMINARE</span><span>LADENDESIGN &amp; EINRICHTUNGEN</span><span>TEAM</span><span>KONTAKT</span></nav>
  <div class="copy">© 2022 K&amp;M GmbH Scherenkunst &amp; Co.</div>
  <div class="social"><span class="dot"></span><span class="dot"></span>
    <svg width="14" height="12" viewBox="0 0 14 12"><path d="M0 1h3l2 7h7l1.5-5H4" fill="none" stroke="#ddd" stroke-width="1.3"/><circle cx="6" cy="10.5" r="1.2" fill="#ddd"/><circle cx="11" cy="10.5" r="1.2" fill="#ddd"/></svg>
  </div>
  <div class="legal"><span>IMPRESSUM</span>|<span>AGB</span>|<span>DATENSCHUTZ</span></div>
</footer>

</body>
</html>
```